A new presentation to our clients

we are a Real Estate agency, our website is www.lirotama.com and it’s time to have a new, fashion and remarcable Business Card. we want to differentiate ourselves from other companies so we want a business card that differentiates us. we want the business card to impact our customers. in the competitive market that we have today, we have to be different and it is this difference that we seek

Target Market(s)

Real Estate Clients

Contact Information for Business Card

We search a totaly diferent card from the usual

Font styles to use
Sans Serif

Colors
e34197

Requirements
Must have
• Logo, adress, phone contact, e-mail, photo, and our website
Nice to have
• We would like to see a modern business card
Should not have
• Houses or building draws

```html
<!DOCTYPE html>
<html lang="en">
<head>
<meta charset="utf-8">
<title>Lirotama Business Card</title>
<link rel="stylesheet" href="https://fonts.googleapis.com/css2?family=Lato:wght@400;700;900&display=swap">
<style>
  :root {
    --backdrop: #2b2b2d;
    --card-slate: #484a53;
    --brand-pink: #e8307a;
    --ink-light: #f2f2f2;
  }
  * { margin: 0; padding: 0; box-sizing: border-box; }
  html, body {
    width: 1200px; height: 1200px; overflow: hidden;
    background: var(--backdrop);
    font-family: "Lato", sans-serif;
  }
  .card {
    position: absolute;
    left: 140px; width: 920px; height: 524px;
    border-radius: 32px;
    overflow: hidden;
  }
  .card--front { top: 48px; background: var(--card-slate); }
  .card--back { top: 640px; background: var(--brand-pink); }

  .wordmark {
    position: absolute;
    font-family: "Lato", sans-serif;
    font-weight: 900;
    font-size: 104px;
    line-height: 1;
    letter-spacing: -1px;
    white-space: nowrap;
  }
  .card--front .wordmark { left: 58px; top: 56px; color: var(--brand-pink); }
  .card--back .wordmark { right: 56px; top: 362px; color: var(--ink-light); }

  .person-name {
    position: absolute; left: 59px; top: 282px;
    font-size: 34px; line-height: 1; font-weight: 400; color: var(--ink-light);
    letter-spacing: 0.5px; white-space: nowrap;
  }
  .person-name .surname { color: var(--brand-pink); }
  .person-role {
    position: absolute; left: 59px; top: 319px;
    font-size: 24px; line-height: 1; color: var(--brand-pink); white-space: nowrap;
  }
  .role-rule {
    position: absolute; left: 218px; top: 335px;
    width: 644px; height: 2px; background: var(--brand-pink);
  }

  .contact-list { position: absolute; left: 60px; top: 367px; list-style: none; }
  .contact-list li {
    display: flex; align-items: center;
    height: 29px; line-height: 29px; font-size: 21px; color: var(--ink-light);
    white-space: nowrap;
  }
  .contact-list svg { width: 20px; height: 20px; margin-right: 16px; flex: none; }
  .contact-list .highlight { color: var(--brand-pink); }

  .address {
    position: absolute; right: 58px; top: 438px;
    text-align: right; font-size: 21px; line-height: 23px; color: var(--ink-light);
    white-space: nowrap;
  }
</style>
</head>
<body>
  <section class="card card--front">
    <div class="wordmark">Lirotama</div>
    <div class="person-name">MARA <span class="surname">VELDEN</span></div>
    <div class="person-role">CEO/manager</div>
    <div class="role-rule"></div>
    <ul class="contact-list">
      <li>
        <svg viewBox="0 0 20 20" fill="none" stroke="#e8307a" stroke-width="2"><rect x="5" y="1" width="10" height="18" rx="2"/><line x1="9" y1="16" x2="11" y2="16"/></svg>
        +123 - 456 - 9789
      </li>
      <li>
        <svg viewBox="0 0 20 20" fill="#e8307a"><path d="M1 7c0-3 4-4 9-4s9 1 9 4v2h-5V7H6v2H1z"/><rect x="4" y="10" width="12" height="7" rx="1"/></svg>
        +123 - 456 - 9789
      </li>
      <li>
        <svg viewBox="0 0 20 20"><rect x="1" y="4" width="18" height="13" fill="#e8307a"/><path d="M1 4l9 7 9-7" fill="none" stroke="#484a53" stroke-width="1.6"/></svg>
        here@yourmail.com
      </li>
      <li>
        <svg viewBox="0 0 20 20" fill="none" stroke="#e8307a" stroke-width="1.6"><circle cx="10" cy="10" r="8"/><ellipse cx="10" cy="10" rx="3.5" ry="8"/><line x1="2" y1="10" x2="18" y2="10"/><line x1="3.5" y1="6" x2="16.5" y2="6"/><line x1="3.5" y1="14" x2="16.5" y2="14"/></svg>
        www.<span class="highlight">yourwebsite</span>.com
      </li>
    </ul>
    <div class="address">Harbor Point 41820<br>Linden Avenue Westbrook</div>
  </section>

  <section class="card card--back">
    <div class="wordmark">Lirotama</div>
  </section>
</body>
</html>
```